Retail Product Label mushrooms

We wish to make a 2x3 inch rectangle product label as shown in the PDF. We wish to use the entire space available to make the words and logo as large as possible. We wish the top 1/3rd to be red with the logo inside it. We wish the bottom 2/3rds to be white with the product name inserted. We still need allocations for the barcode weight etc. as shown in the image uploaded.

Target Market(s)

Retail Label

Industry/Entity Type

Fresh Produce mushrooms

Colors
EB3D1F
EC4F4E
F09395
F8D3D4
FCEDEE

Requirements
Must have
• All included
Nice to have
• Shiitake label is best example of what we seek in a rectangle design
Should not have
• You must include all information in the example (weight barcode area, etc.)

```html
<!DOCTYPE html>
<html lang="en">
<head>
<meta charset="utf-8">
<title>Timberline Table – Shiitake Labels</title>
<link rel="stylesheet" href="https://fonts.googleapis.com/css2?family=Montserrat:wght@400;700;800&family=Saira+Condensed:wght@500;600;700&display=swap">
<style>
  :root {
    --page: #ffffff;
    --white: #ffffff;
    --brown: #6b5a3a;
    --green: #2fa83f;
    --ink: #1a1a1a;
  }
  html, body { margin: 0; padding: 0; overflow: hidden; background: var(--page); }
  .canvas { position: relative; width: 1200px; height: 1000px; overflow: hidden; background: var(--page); }

  .label { position: absolute; top: 151px; width: 509px; height: 732px; }
  .label--whole  { left: 54px;  --base: #fe0000; --shade: #9a0000; --accent: #ff2a00; }
  .label--sliced { left: 639px; --base: #ff4500; --shade: #9a300c; --accent: #ff4500; }

  .label__art { position: absolute; left: 0; top: -32px; width: 509px; height: 764px; overflow: visible;
    filter: drop-shadow(2px 4px 4px rgba(0,0,0,.3)); }
  .label__body { fill: var(--white); stroke: var(--base); stroke-width: 10; }
  .label__top { fill: var(--base); }
  .label__forest-top { fill: var(--shade); opacity: .55; }

  .text { position: absolute; left: 0; width: 509px; text-align: center; line-height: 1; margin: 0; }
  .brand { top: 50px; font-family: "Saira Condensed", sans-serif; font-weight: 700; font-size: 62px;
    color: var(--white); letter-spacing: .02em; }
  .fresh { top: 163px; font-family: "Saira Condensed", sans-serif; font-weight: 600; font-size: 54px; color: var(--green); }
  .origin { top: 227px; font-family: "Montserrat", sans-serif; font-weight: 700; font-size: 22px; letter-spacing: .2em; color: var(--brown); }
  .product { top: 274px; font-family: "Montserrat", sans-serif; font-weight: 800; font-size: 76px; letter-spacing: .01em; color: var(--brown); }
  .variety { top: 377px; font-family: "Saira Condensed", sans-serif; font-weight: 600; font-size: 50px; color: var(--brown); }
  .variety--spaced { letter-spacing: .2em; padding-left: .2em; box-sizing: border-box; }
  .variety__cut { color: var(--accent); }

  .rule { position: absolute; left: 60px; top: 450px; width: 389px; height: 3px; background: var(--base); }

  .weight { top: 463px; font-family: "Saira Condensed", sans-serif; font-weight: 500; font-size: 38px; color: var(--brown); letter-spacing: .06em; }
  .weight__value { font-size: 50px; font-weight: 600; letter-spacing: 0; color: var(--base); }
  .storage { top: 511px; font-family: "Saira Condensed", sans-serif; font-weight: 600; font-size: 28px; color: var(--brown); }
  .web { top: 545px; font-family: "Saira Condensed", sans-serif; font-weight: 700; font-size: 30px; color: var(--base); letter-spacing: .08em; }

  .code-box { position: absolute; left: 96px; top: 590px; width: 318px; height: 124px;
    background: var(--white); border: 3px solid var(--base); box-sizing: border-box; }

  .caption { position: absolute; left: 0; top: 922px; width: 1200px; text-align: center;
    font-family: "Montserrat", sans-serif; font-weight: 400; font-size: 29px; color: var(--ink); margin: 0; }
</style>
</head>
<body>
<div class="canvas">

  <section class="label label--whole">
    <svg class="label__art" viewBox="0 -32 509 764">
      <defs>
        <clipPath id="shape-whole"><path d="M0,25 Q0,0 25,0 H150 Q175,0 192,-15 Q220,-32 254,-32 Q288,-32 316,-15 Q333,0 358,0 H484 Q509,0 509,25 V707 Q509,732 484,732 H25 Q0,732 0,707 Z"/></clipPath>
      </defs>
      <path class="label__body" d="M0,25 Q0,0 25,0 H150 Q175,0 192,-15 Q220,-32 254,-32 Q288,-32 316,-15 Q333,0 358,0 H484 Q509,0 509,25 V707 Q509,732 484,732 H25 Q0,732 0,707 Z"/>
      <g clip-path="url(#shape-whole)">
        <path class="label__top" d="M-10,-40 H520 V176 Q254,124 -10,176 Z"/>
        <path class="label__forest-top" role="img" aria-label="Pine forest silhouette behind the brand name" d="M-10,176 V110 Q254,70 520,110 V176 Q254,124 -10,176 Z"/>
      </g>
    </svg>

    <p class="text brand">TIMBERLINE TABLE</p>
    <p class="text fresh">FRESH</p>
    <p class="text origin">PRODUCT OF USA</p>
    <p class="text product">SHIITAKE</p>
    <p class="text variety variety--spaced">MUSHROOMS</p>
    <div class="rule"></div>
    <p class="text weight">NET WT <span class="weight__value">3.5</span> OZ</p>
    <p class="text storage">KEEP REFRIDGERATED</p>
    <p class="text web">WWW.TIMBER-TABLE.COM</p>
    <div class="code-box"></div>
  </section>

  <section class="label label--sliced">
    <svg class="label__art" viewBox="0 -32 509 764">
      <defs>
        <clipPath id="shape-sliced"><path d="M0,25 Q0,0 25,0 H150 Q175,0 192,-15 Q220,-32 254,-32 Q288,-32 316,-15 Q333,0 358,0 H484 Q509,0 509,25 V707 Q509,732 484,732 H25 Q0,732 0,707 Z"/></clipPath>
      </defs>
      <path class="label__body" d="M0,25 Q0,0 25,0 H150 Q175,0 192,-15 Q220,-32 254,-32 Q288,-32 316,-15 Q333,0 358,0 H484 Q509,0 509,25 V707 Q509,732 484,732 H25 Q0,732 0,707 Z"/>
      <g clip-path="url(#shape-sliced)">
        <path class="label__top" d="M-10,-40 H520 V176 Q254,124 -10,176 Z"/>
        <path class="label__forest-top" role="img" aria-label="Pine forest silhouette behind the brand name" d="M-10,176 V110 Q254,70 520,110 V176 Q254,124 -10,176 Z"/>
      </g>
    </svg>

    <p class="text brand">TIMBERLINE TABLE</p>
    <p class="text fresh">FRESH</p>
    <p class="text origin">PRODUCT OF USA</p>
    <p class="text product">SHIITAKE</p>
    <p class="text variety"><span class="variety__cut">SLICED</span> MUSHROOMS</p>
    <div class="rule"></div>
    <p class="text weight">NET WT <span class="weight__value">3.5</span> OZ</p>
    <p class="text storage">KEEP REFRIDGERATED</p>
    <p class="text web">WWW.TIMBER-TABLE.COM</p>
    <div class="code-box"></div>
  </section>

  <p class="caption">Version 1</p>
</div>
</body>
</html>
```